Business Card and Logo tweak for a Language Boarding School

we are a boadring langauge school for under 18 international student.
We call ourselves " HCSC" - Harwick Crossway Study Centre
We are one of the TQ "tidewater quarters" Melbourne campus for TQ high school preparation program.

our address is 14 Orrin Lane Brighton 3187
Ph: 03 95550142
Email: info@myhcsc-example.com
Website: www.myhcsc-example.com

We have our HCSC logo, but not very satisfied. May be you can tweak it furhter with the fond or formations.

Basically the business card list all relevant info on one side and list all our programs on the other side.

The program we have:
ELICOS with Boarding for U18 Students
HSP-High School Preparation Program
PSP- Primary School Preparation Program
Junior Holiday Program & Study Tours
After School Tutoring
Student Wellbeing and Counselling

```html
<!DOCTYPE html>
<html lang="en">
<head>
<meta charset="utf-8">
<title>Harwick Crossway Study Centre – Business Card</title>
<link href="https://fonts.googleapis.com/css2?family=Arimo:wght@400&family=Carlito:wght@400;700&display=swap" rel="stylesheet">
<style>
  :root {
    --backdrop: #eceeed;
    --card-yellow: #fdea00;
    --brand-green: #86b22f;
    --card-white: #ffffff;
    --ink: #231f20;
  }
  html, body {
    margin: 0;
    padding: 0;
    width: 1200px;
    height: 1079px;
    overflow: hidden;
    background: var(--backdrop);
  }
  .canvas {
    position: relative;
    width: 1200px;
    height: 1079px;
  }
  .card {
    position: absolute;
    left: 314px;
    width: 572px;
    height: 326px;
    border-radius: 18px;
    overflow: hidden;
  }
  .card--front { top: 171px; background: var(--card-yellow); }
  .card--back  { top: 582px; background: var(--card-white); }
  .card__art {
    position: absolute;
    inset: 0;
    width: 100%;
    height: 100%;
  }
  .brand {
    position: absolute;
    left: 58px;
    top: 56px;
    display: flex;
    align-items: center;
    gap: 14px;
  }
  .brand__dot {
    width: 44px;
    height: 44px;
    border-radius: 50%;
    background: var(--ink);
    flex: none;
  }
  .brand__name {
    margin: 0;
    font-family: "Arimo", Arial, sans-serif;
    font-weight: 400;
    font-size: 22px;
    line-height: 20px;
    letter-spacing: -0.3px;
    text-transform: uppercase;
    color: var(--ink);
  }
  .contact {
    position: absolute;
    right: 28px;
    top: 22px;
    margin: 0;
    text-align: right;
    font-family: "Carlito", Calibri, sans-serif;
    font-size: 17.5px;
    line-height: 23.7px;
    color: var(--brand-green);
    font-style: normal;
  }
  .contact__org {
    display: block;
    font-weight: 700;
  }
  .programs {
    list-style: none;
    margin: 0;
    padding: 0;
  }
</style>
</head>
<body>
<main class="canvas">
  <section class="card card--front" aria-label="Card front">
    <svg class="card__art" viewBox="0 0 572 326" aria-hidden="true">
      <path d="M 160 345 C 210 240, 300 205, 380 185 S 480 60, 610 0"
            fill="none" stroke="var(--brand-green)" stroke-width="34" stroke-linecap="round"/>
    </svg>
    <div class="brand">
      <span class="brand__dot"></span>
      <h1 class="brand__name">Harwick<br>Crossway<br>Study Centre</h1>
    </div>
  </section>

  <section class="card card--back" aria-label="Card back">
    <svg class="card__art" viewBox="0 0 572 326" aria-hidden="true">
      <circle cx="7" cy="80" r="190" fill="none" stroke="var(--card-yellow)" stroke-width="36"/>
    </svg>
    <address class="contact">
      <span class="contact__org">HARWICK CROSSWAY<br>STUDY CENTRE</span>
      14 Orrin Lane Brighton 3187<br>
      03 95550142<br>
      info@myhcsc-example.com<br>
      www.myhcsc-example.com
      <ul class="programs">
        <li>ELICOS with Boarding for U18 Students</li>
        <li>HSP-High School Preparation Program</li>
        <li>PSP-Primary School Preparation Program</li>
        <li>Junior Holiday Program &amp; Study Tours</li>
        <li>After School Tutoring</li>
        <li>Student Wellbeing and Counselling</li>
      </ul>
    </address>
  </section>
</main>
</body>
</html>
```